website design + images

We need a very appealing website design, layout and images for a sales analytics and sales productivity services company based in San Ramon, California. We need a good design for the home page and a template for all other pages (total 2 designs), and images for all inner pages (center column/banner images, and right hand top corner small images). There are about 18 inner pages.
Updates

Our existing website is www.corvexa.com
Our corporate colours are the ones that are there on the website. The logo is also shown. We will be changing the tagline to "Powering Sales Growth" or equivalent of that.

Please use the document "website for corvexa - template v2.doc" that I just uploaded for any reference to the content, navigation and wireframes. A few more clarifications are provided mainly for the link "Solutions".

Hemant Loravi

Hi,
We just uploaded ver 4 of the website template. There is more elaboration provided around the sublinks / sections for Solutions. Pls review and do get back if you need any clarifications.

Rgds
Hemant Loravi

Hi all,
We have so far received a few good designs. The designs are more or less on the right track. I would like to urge all of you to use the content and navigation provided in the document attached to our brief "website for corvexa - template v4.doc".  Please DO NOT use the content in our existing website www.corvexa.com . That is very old. We mentioned it only for reference to colour theme and broad details.

We have totally 13 sections in Solutions pages. They may be designed as a tree of links - first level sublinks - second level sublinks or links - first level sublinks and the remaining as sections within the first level sublinks pages. The page design would remain the same for all inner pages except careers. But after finalizing the design for the inner page, we will need images for the different inner pages.

Rgds
Hemant Loravi

Hi,
Thank you all for participation and very good designs. We are quite happy with what we have seen. We have now shortlisted about 4 vendors and sending invididual feedback to them for further improvement. We will be finalizing by Monday or Tuesday.  To the vendors who do not get feedback from us, thank you very much for participation. We may still do business in future for some of our other needs. 
The following are the process steps / expectations going forward, 
1. Feedback to the shortlisted designers and inviting improvements.
2. Review of the improved designs and further shortlist & feedback or direct finalization.
3. The design should be in 1024*768
2. Number of page designs = 2 (home page, inner page).
4. Home page design: instead of delivery model and customers, show one link "Why Us".
4. Solutions page design:  We will be needing an image in center column of solutions page that in a nutshell gives all the different types of solutions we provide. The entire set of solutions is in our attached document website for corvexa - template v4 and I am just uploading v5 with more description on sublinks.
5. After selection, we will be needing images for all the solution pages (total 12 pages under solutions + one solutions page), 1 image for Why Us?, 1 for Careers, and 3 for company (about us/ team, core values, ...) = total 18

Rgds
Hemant Loravi

Target Market(s)

We are a sales analytics and sales productivity services company. We help B2B companies with: sales planning; sales operations and sales measurement. The characteristics of our customers are:
- B2B medium enterprises (USD 100M- USD 2B in revenue) in the US
- Primary target verticals are: high-tech, engineering and professional services firms
- Our primary target customers titles are VP of Sales or VP of marketing; we could be selling to the CEO at companies with revenues below $200M

Industry/Entity Type

Consulting

Requirements
Must have
• - Clean, uncluttered design
• - Easy navigation; minimum clicks
Nice to have
• We have already built a content management system and wireframes for this site. To the extent possible, it would be great to leverage the wireframe structure we built, provided you don’t have to compromise on the look and feel and navigation of the site. Below is what we currently have as banner sizes and resolutions are:
• Home page banner size: 950 * 250’
• All pages – center top - image size: 558 * 160
• All pages – right hand top image – 175*135’

```html
<!DOCTYPE html>
<html lang="en">
<head>
<meta charset="utf-8">
<title>Corvexa — Career Form</title>
<link href="https://fonts.googleapis.com/css2?family=Arimo:ital,wght@0,400;0,700;1,400&display=swap" rel="stylesheet">
<style>
  :root{
    --stage-top:#c4c4c4;
    --stage-bottom:#e2e2e2;
    --sheet:#ffffff;
    --navy:#1d2c5e;
    --green:#4c9a3c;
    --ink:#111111;
    --muted:#555555;
    --field-border:#a9a9a9;
    --nav-light:#f1f1f1;
    --nav-mid:#dcdcdc;
    --nav-dark:#c9c9c9;
    --divider:#bdbdbd;
    --brand-blue:#2a6fb8;
  }
  *{box-sizing:border-box;margin:0;padding:0}
  html,body{width:1200px;height:912px;overflow:hidden}
  body{
    background:linear-gradient(var(--stage-top),var(--stage-bottom));
    font-family:"Arimo",Arial,sans-serif;
    color:var(--ink);
    position:relative;
  }
  .page{
    position:absolute;left:139px;top:74px;width:912px;height:768px;
    background:var(--sheet);
    box-shadow:0 0 4px rgba(0,0,0,.35);
  }
  .brand{position:absolute;left:39px;top:16px;width:140px;text-align:center}
  .brand-mark{display:block;width:46px;height:46px;border-radius:50%;background:var(--brand-blue);margin:0 auto 6px}
  .brand-name{font-size:15px;font-weight:700;color:var(--navy);letter-spacing:.5px}
  .brand-tagline{font-size:12px;color:var(--green);margin-top:1px;white-space:nowrap}

  .main-nav{
    position:absolute;left:0;top:113px;width:912px;height:49px;
    background:linear-gradient(var(--nav-light),var(--nav-mid) 55%,var(--nav-dark));
    border-top:1px solid #e8e8e8;
    box-shadow:0 2px 3px rgba(0,0,0,.15);
  }
  .main-nav a{
    position:absolute;top:0;height:49px;display:flex;align-items:center;justify-content:center;
    text-align:center;font-size:13.5px;line-height:17px;color:var(--navy);text-decoration:none;
    border-left:1px solid var(--divider);
  }
  .main-nav a.last{border-right:1px solid var(--divider)}

  .banner-photo{
    position:absolute;left:3px;top:163px;width:405px;height:289px;
    background:linear-gradient(100deg,#d7dde2 0%,#b9c1c8 35%,#eef1f3 70%,#cfd5da 100%);
  }
  .banner-backdrop{
    position:absolute;left:408px;top:163px;width:329px;height:293px;
    background:linear-gradient(90deg,#f7f7f7 0%,#eeeeee 55%,#dcdcdc 80%,#f2f2f2 100%);
  }

  .form-title{position:absolute;left:430px;top:192px;font-size:17px;color:var(--green)}
  .form-note{position:absolute;left:459px;top:216px;font-size:10.5px;font-style:italic}
  .label{position:absolute;font-size:10.5px;line-height:13px}
  .section-label{position:absolute;font-size:11px;font-weight:700;color:var(--green)}
  .field{
    position:absolute;width:143px;height:21px;background:#fff;
    border:1px solid var(--field-border);
    box-shadow:inset 0 2px 3px rgba(0,0,0,.12);
  }
  .field.area{height:50px}
  .footer-links{position:absolute;left:0;width:912px;top:742px;text-align:center;font-size:10.5px;color:var(--muted)}
</style>
</head>
<body>
<div class="page">
  <header class="brand">
    <span class="brand-mark"></span>
    <div class="brand-name">CORVEXA</div>
    <div class="brand-tagline">Powering Sales Growth</div>
  </header>

  <nav class="main-nav">
    <a href="#" style="left:88px;width:100px">Home</a>
    <a href="#" style="left:188px;width:106px">Solutions</a>
    <a href="#" style="left:294px;width:108px">Why Us ?</a>
    <a href="#" style="left:402px;width:101px">Delivery</a>
    <a href="#" style="left:503px;width:98px">Industry<br>Vertical</a>
    <a href="#" style="left:601px;width:104px">Company</a>
    <a href="#" class="last" style="left:705px;width:119px">Career</a>
  </nav>

  <div class="banner-photo" role="img" aria-label="Photo of business team walking through a bright glass-walled office"></div>
  <div class="banner-backdrop" role="img" aria-label="Faded photo of a bright modern office interior"></div>

  <form class="career-form">
    <h1 class="form-title">Career Form</h1>
    <p class="form-note">Please complete the following details. All fields marked with * are mandatory</p>

    <span class="label" style="left:457px;top:239px">*Full Name</span>
    <span class="field" style="left:591px;top:234px"></span>

    <span class="label" style="left:457px;top:277px">*Date of Birth</span>
    <span class="field" style="left:591px;top:273px"></span>

    <span class="section-label" style="left:459px;top:309px">Contact Details</span>
    <span class="label" style="left:459px;top:334px">*Address</span>
    <span class="field area" style="left:592px;top:323px"></span>

    <span class="label" style="left:752px;top:314px">*City</span>
    <span class="field" style="left:750px;top:332px"></span>
    <span class="label" style="left:750px;top:364px">*State</span>
    <span class="field" style="left:750px;top:379px"></span>

    <span class="label" style="left:457px;top:418px">*Contact No</span>
    <span class="field" style="left:591px;top:414px"></span>

    <span class="label" style="left:457px;top:451px">*Email</span>
    <span class="field" style="left:591px;top:448px"></span>

    <span class="section-label" style="left:458px;top:486px">Professional Details</span>

    <span class="label" style="left:459px;top:520px">*Qualification</span>
    <span class="field" style="left:591px;top:516px"></span>

    <span class="label" style="left:459px;top:556px">*Work Experience</span>
    <span class="field" style="left:591px;top:552px"></span>

    <span class="label" style="left:458px;top:593px">Present Company Name</span>
    <span class="field" style="left:591px;top:588px"></span>

    <span class="label" style="left:460px;top:629px">Address</span>
    <span class="field area" style="left:591px;top:628px"></span>
  </form>

  <footer class="footer-links">Copyright, disclaimer, contact us</footer>
</div>
</body>
</html>
```